Meadowlark Soaps Business Card

The new business card design will incorporate my new logo components designed by one of your designers. Meadowlark Soaps creates high quality soaps and bath products. They would be suited for a Spa, Bed and Breakfast, Boutique environment. The look should be a white background.
Classy, soft and using the colour palet of the logo. The card will be two sided.

Reason: Need more time to make some changes and decide.

Target Market(s)

Looking to appeal to an upper end market. Spas, boutiques, independent gift stores, bridal salons, bed and breakfast, etc. I want the card to impart a sense of elegance, tranquility and Meadowlark. But also quality and value.

Industry/Entity Type

Business

Font styles to use
Sans Serif
Script

Requirements
Must have
• My logo on the front. But also on the back but faded out to allow written notes on the back.
On the front : Marta Quennell
Owner/Creator
47 Ashcombe Rd
Alderbrook, Ont K7R 2M5
555.014.2938
Creating Quality Handcrafted Soaps And Bath Products
Custom and Wholesale Orders Welcome
Www.meadowlarksoaps.ca
Www.facebook.com / MeadowlarkSoapandBath
info@meadowlarksoaps.ca

```html
<!DOCTYPE html>
<html lang="en">
<head>
<meta charset="utf-8">
<title>Meadowlark Soaps – Business Cards</title>
<link href="https://fonts.googleapis.com/css2?family=Lato:wght@400;700&family=Pinyon+Script&display=swap" rel="stylesheet">
<style>
  :root {
    --backdrop: #4a4a4a;
    --card: #ffffff;
    --teal: #7fb3a6;
    --teal-text: #7fa99d;
    --teal-faint: #e3eeeb;
    --faded-mark: #f1f6f4;
    --faded-name: #e6efec;
    --sand: #e6d6c5;
    --sand-text: #e0c3a6;
  }
  * { box-sizing: border-box; margin: 0; padding: 0; }
  html, body { width: 1200px; height: 1000px; overflow: hidden; }
  body { background: var(--backdrop); position: relative; font-family: "Lato", sans-serif; }

  .card {
    position: absolute; width: 490px; height: 286px;
    background: var(--card); overflow: hidden;
  }
  .card--front-a { left: 88px; top: 163px; }
  .card--back-a  { left: 620px; top: 163px; }
  .card--front-b { left: 88px; top: 551px; }
  .card--back-b  { left: 620px; top: 551px; }

  .wave { position: absolute; left: 0; top: 0; width: 490px; height: 286px; }

  .brand { position: absolute; left: 22px; top: 34px; width: 240px; text-align: center; }
  .brand__mark { width: 118px; height: 118px; border-radius: 50%; background: var(--teal-faint); margin: 0 auto 12px; }
  .brand__name { font-size: 25px; color: var(--teal-text); letter-spacing: .5px; line-height: 1.1; }

  .contact { position: absolute; left: 293px; top: 32px; color: var(--teal-text); }
  .contact__name { font-family: "Pinyon Script", cursive; font-size: 28px; line-height: 1; }
  .contact--sand .contact__name { color: var(--sand-text); }
  .contact__role { font-size: 13.5px; margin-top: 5px; }
  .contact__address { font-size: 11.5px; line-height: 18px; margin-top: 15px; }
  .contact__links { list-style: none; font-size: 11.5px; font-weight: 700; line-height: 19px; margin-top: 11px; }
  .contact__links li { display: flex; align-items: center; gap: 6px; }
  .contact__links svg { width: 12px; height: 12px; flex: none; }

  .tagline { position: absolute; left: 0; width: 100%; text-align: center; font-size: 13px; color: var(--teal-text); }
  .notes { position: absolute; font-family: "Pinyon Script", cursive; font-size: 26px; color: var(--teal-text); }
  .faded-brand { position: absolute; left: 0; width: 100%; text-align: center; }
  .faded-brand__mark { width: 130px; height: 130px; border-radius: 50%; background: var(--faded-mark); margin: 0 auto 8px; }
  .faded-brand__name { font-size: 24px; color: var(--faded-name); letter-spacing: .5px; }
</style>
</head>
<body>

<!-- Front, version A -->
<section class="card card--front-a">
  <svg class="wave" viewBox="0 0 490 286" aria-hidden="true">
    <path d="M0 252 C90 258 170 290 270 274 C360 258 420 232 490 226 L490 286 L0 286 Z" fill="var(--sand)"/>
    <path d="M6 240 C80 258 150 290 250 276 C340 262 400 210 490 206" fill="none" stroke="var(--teal)" stroke-width="6"/>
  </svg>
  <div class="brand">
    <div class="brand__mark"></div>
    <div class="brand__name">Meadowlark Soaps</div>
  </div>
  <div class="contact">
    <div class="contact__name">Marta Quennell</div>
    <div class="contact__role">Owner/Creator</div>
    <div class="contact__address">47 Ashcombe Rd<br>Alderbrook,Ont K7R 2M5</div>
    <ul class="contact__links">
      <li><svg viewBox="0 0 12 12"><path d="M3 1 L5 3 L4 5 Q5 7 7 8 L9 7 L11 9 L9 11 Q4 10 1 3 Z" fill="var(--sand-text)"/></svg>555.014.2938</li>
      <li><svg viewBox="0 0 12 12"><circle cx="6" cy="6" r="5" fill="none" stroke="var(--sand-text)"/><path d="M1 6 H11 M6 1 Q3 6 6 11 M6 1 Q9 6 6 11" fill="none" stroke="var(--sand-text)" stroke-width=".8"/></svg>www.meadowlarksoaps.ca</li>
      <li><svg viewBox="0 0 12 12"><rect x="2" y="2" width="8" height="8" fill="var(--sand-text)"/></svg>MeadowlarkSoapandBath</li>
    </ul>
  </div>
</section>

<!-- Back, version A -->
<section class="card card--back-a">
  <div class="faded-brand" style="top:52px">
    <div class="faded-brand__mark"></div>
    <div class="faded-brand__name">Meadowlark Soaps</div>
  </div>
  <svg class="wave" viewBox="0 0 490 286" aria-hidden="true">
    <path d="M0 252 C90 258 170 290 270 274 C360 258 420 232 490 226 L490 286 L0 286 Z" fill="var(--sand)"/>
    <path d="M6 240 C80 258 150 290 250 276 C340 262 400 210 490 206" fill="none" stroke="var(--teal)" stroke-width="6"/>
  </svg>
  <p class="tagline" style="top:31px">Creating Quality Handcrafted Soaps And Bath Products</p>
  <p class="notes" style="left:32px; top:62px">Notes:</p>
</section>

<!-- Front, version B -->
<section class="card card--front-b">
  <svg class="wave" viewBox="0 0 490 286" aria-hidden="true">
    <path d="M0 252 C90 258 170 290 270 274 C360 258 420 232 490 226 L490 286 L0 286 Z" fill="var(--sand)"/>
    <path d="M6 240 C80 258 150 290 250 276 C340 262 400 210 490 206" fill="none" stroke="var(--teal)" stroke-width="6"/>
  </svg>
  <div class="brand">
    <div class="brand__mark"></div>
    <div class="brand__name">Meadowlark Soaps</div>
  </div>
  <div class="contact contact--sand">
    <div class="contact__name">Marta Quennell</div>
    <div class="contact__role">Owner/Creator</div>
    <div class="contact__address">47 Ashcombe Rd<br>Alderbrook,Ont K7R 2M5</div>
    <ul class="contact__links">
      <li><svg viewBox="0 0 12 12"><path d="M3 1 L5 3 L4 5 Q5 7 7 8 L9 7 L11 9 L9 11 Q4 10 1 3 Z" fill="var(--sand-text)"/></svg>555.014.2938</li>
      <li><svg viewBox="0 0 12 12"><circle cx="6" cy="6" r="5" fill="none" stroke="var(--sand-text)"/><path d="M1 6 H11 M6 1 Q3 6 6 11 M6 1 Q9 6 6 11" fill="none" stroke="var(--sand-text)" stroke-width=".8"/></svg>www.meadowlarksoaps.ca</li>
      <li><svg viewBox="0 0 12 12"><rect x="2" y="2" width="8" height="8" fill="var(--sand-text)"/></svg>MeadowlarkSoapandBath</li>
    </ul>
  </div>
</section>

<!-- Back, version B -->
<section class="card card--back-b">
  <div class="faded-brand" style="top:48px">
    <div class="faded-brand__mark"></div>
    <div class="faded-brand__name">Meadowlark Soaps</div>
  </div>
  <p class="notes" style="left:28px; top:28px">Notes:</p>
  <p class="tagline" style="top:249px">Creating Quality Handcrafted Soaps And Bath Products</p>
</section>

</body>
</html>
```